Professional Lawn Treatment flyer (double sided) needed for established gardening company

We are an established and trusted gardening company in Swindon, UK, and are about to launch a new Lawn Treatment Service. This will be marketed to both existing and new customers and needs to reflect our current professional image. The flyer will need to be double-sided, portrait orientation and correctly sized so to be printed on A5.

If you look on our website www.pelhamgardening.co.uk, you will see our colours are purple and green. We would like you to use these exact shades of purple and green in your design.

As part of the design, we will need you to put together an infographic table to show our packages. I have attached a spreadsheet which explains these packages but I will need you to create a visually appealing table that fits in with the overall design of the flyer. I don't want you to simply cut and paste my basic table into the design.

In terms of what needs to be included, I have tried to be as specific as possible here but please feel free to message me if you need any further information or clarification.

FRONT SIDE:
The title of our service is:
Expert Lawn Treatment Service

Our strapline will need to be included somewhere:
"Lawn care by your local gardening expert"

The front side of the flyer will need to contain our logo - different versions of which can be found within my dropbox folder here...

https://www.filecrate.net/sh/k7bq24nwxe9/QWT8PmRzLxKd3VuYcH0BnJeFa?dl=0

The front side will need to contain a main image (although feel free to add more if you have anything suitable). I have included a picture in the dropbox folder titled "Front side image" which we would like used. I've also included in the folder an adobe image of grass which you may or may not like to use on either front or back.

Somewhere on both the front and back sides, you will need to include our contact details:
01632 960481
www.pelhamgardening.co.uk/lawncare

The front side should show what treatments we currently have available. These are:

- Lawn Fertilising
- Scarification
- Aeration
- Weed Control
- Moss Control
- Hydration Booster
- Kempix
- Turfing & Renovation

"Select a one-off treatment or choose from one of our specially created lawn care packages."

BACK SIDE:
On the back, we will still need our logo and contact details but the image we'd like used should be the one in the dropbox folder titled "Back side image". Again, if you have any other images you feel would also work, then please feel free to add them.

The back side is to contain a bit more information and be a bit 'wordier' and so can you please include the following 2 paragraphs:

"As expert gardeners, we are passionate about horticulture and working to bring out the very best in your garden. When we work in your garden, we look at it and treat it with the same care and attention as if it were our own, before handing it back for you to enjoy. Our passion doesn't end at just trees and shrubs though. Your grass is as much of a living, breathing plant as your shrubs and we therefore utilise our expert horticultural knowledge to ensure your lawn thrives and reaches its fullest potential.

Lawn care isn't just about applying a fertiliser. It's about really understanding your lawn and being able to use extensive knowledge and experience to diagnose and treat issues. It therefore stands to reason that you should employ an expert to bring out the best in your lawn which is why we at Pelham Gardening Services have created a superior lawn care service that will keep your lawn looking lush, green and healthy all year round."

I referred at the very top of this brief to the fact we will need an infographic table created to show the different lawn care packages available. You see from the PDF table I created that we have 3 packages; Standard, Enhanced and Premium. Please create a visually appealing table which sets out the differences between our packages and include it on the back page.

Finally, somewhere we would like reference to the other gardening services we do. It's only to be something small as it isn't the main focus of the flyer but we think it would be good to mention what else we do. To re-iterate, it isnt to be big. I still want the main focus to be lawn care but if you could somehow reference that we also do the following services, that would be good. I will leave it to you to decide where on the flyer it fits in best, be it the front or back:

- Lawn mowing
- Shrub pruning
- Hedge trimming
- Weed killing
- Garden clearance & tidy-up
- Planting & design
- Regular Garden Maintenance
- Turfing
- Fencing
- Gutter clearance

I think thats it. I look forward to your designs!
Ps. Don't forget the dropbox folder:

Target Market(s)

Professional men/women aged 25+
Retired aged 65+

Industry/Entity Type

Home And Garden

Font styles to use
Sans Serif

Colors
6b449b
9bcb3c

Requirements
Must have
• Our company colours; purple and green; as per our website www.pelhamgardening.co.uk. I've selected purple and green on this brief just to highlight the colours needed but please be sure to use the exact shades from our website and NOT the shade of purple and green that were selected on this brief.
• All the wording as explained in the main project brief.
Nice to have
• I want the flyer to be bold, eye-catching and modern.
• We particularly like the font Trebuchet MS for general copy but please feel free to use any other font for bolder, main titles.
Should not have
• We don't want anything gimmicky. No cheesy marketing.
• We only want professional looking designs. With the greatest of respect, if you're just starting out or don't really do design but think you'll use this as practise, please don't waste your or our time. We've previously run contests for other projects where we've had designs submitted that have clearly been done on MS Word and used Clipart and Wordart. That's really not what we are looking for.

```html
<!DOCTYPE html>
<html lang="en">
<head>
<meta charset="utf-8">
<title>Pelham Gardening Services – Expert Lawn Treatment Flyer</title>
<link href="https://fonts.googleapis.com/css2?family=Roboto:wght@300;400;500;700&family=Roboto+Condensed:wght@700&display=swap" rel="stylesheet">
<style>
  :root {
    --purple: #5b2696;
    --purple-deep: #4a1c84;
    --purple-light: #6f3aa8;
    --green: #8cc63f;
    --green-dark: #5f9a22;
    --white: #ffffff;
    --page: #e9e8ee;
  }
  * { box-sizing: border-box; margin: 0; padding: 0; }
  html, body { width: 1200px; height: 1200px; overflow: hidden; }
  body {
    background: var(--page);
    font-family: "Roboto", sans-serif;
    position: relative;
  }
  .flyer {
    position: absolute;
    top: 224px;
    width: 533px;
    height: 752px;
    background: var(--purple);
    overflow: hidden;
    box-shadow: 0 6px 18px rgba(40, 20, 70, .25);
    color: var(--white);
  }
  .flyer--front { left: 51px; }
  .flyer--back { left: 616px; }
  .layer { position: absolute; left: 0; top: 0; }

  /* logo diamond */
  .logo-badge {
    position: absolute;
    width: 144px; height: 144px;
  }
  .logo-badge svg { position: absolute; inset: 0; }
  .logo-name {
    position: absolute; inset: 0;
    display: flex; flex-direction: column; align-items: center; justify-content: center;
    color: var(--purple);
    font-family: "Roboto", sans-serif;
    font-weight: 500;
    font-size: 19px;
    line-height: 1.05;
    text-align: center;
  }
  .logo-name small { font-size: 8px; letter-spacing: 1px; text-transform: uppercase; font-weight: 500; }

  /* front */
  .headline {
    position: absolute; left: 0; width: 500px; top: 340px;
    text-align: center;
  }
  .headline__main {
    font-family: "Roboto Condensed", sans-serif;
    font-weight: 700; font-size: 47px; line-height: 1; letter-spacing: -.5px;
  }
  .headline__main span { color: var(--green); }
  .headline__sub {
    font-weight: 700; font-size: 19px; letter-spacing: 3.2px; margin-top: 5px;
  }
  .headline__strap { font-weight: 400; font-size: 14px; margin-top: 9px; }

  .services-tab {
    position: absolute; left: 29px; top: 448px; width: 184px; height: 42px;
    background: linear-gradient(180deg, #9ed24f, var(--green-dark));
    border-radius: 10px 4px 10px 4px;
    transform: skewX(-6deg);
    box-shadow: 0 3px 6px rgba(0,0,0,.3);
  }
  .services-tab h2 {
    transform: skewX(6deg);
    font-family: "Roboto Condensed", sans-serif; font-weight: 700; font-size: 23px;
    line-height: 42px; text-align: center;
  }
  .services-list {
    position: absolute; left: 34px; top: 504px; list-style: none;
    font-family: "Roboto Condensed", sans-serif; font-weight: 700; font-size: 16.5px;
    line-height: 19.4px; text-transform: uppercase;
  }
  .services-note {
    position: absolute; left: 0; width: 533px; top: 680px;
    text-align: center; font-size: 11px; font-weight: 300;
  }

  /* contact band */
  .contact-band {
    position: absolute; left: 0; bottom: 0; width: 533px; height: 48px;
  }
  .contact-phone {
    position: absolute; left: 14px; bottom: 4px;
    font-family: "Roboto Condensed", sans-serif; font-weight: 700; font-size: 34px;
    letter-spacing: -.3px; color: var(--white);
    text-shadow: 0 2px 3px rgba(0,0,0,.45);
  }
  .contact-url {
    position: absolute; right: 20px; bottom: 11px;
    font-weight: 700; font-size: 13px; color: var(--purple);
  }

  /* back */
  .intro {
    position: absolute; left: 29px; top: 28px; width: 482px;
    font-size: 10px; line-height: 14.5px; font-weight: 400;
  }
  .intro p + p { margin-top: 16px; }

  .packages {
    position: absolute; left: 54px; top: 207px; width: 422px;
  }
  .packages__title {
    background: var(--green); border-radius: 5px 5px 0 0;
    font-weight: 700; font-size: 13px; text-align: center; line-height: 19px;
  }
  .packages table {
    width: 100%; border-collapse: collapse;
    border: 1px solid rgba(255,255,255,.85); border-top: none;
    font-size: 11px; font-weight: 700;
  }
  .packages th { height: 21px; font-weight: 700; }
  .packages td { height: 17px; }
  .packages th, .packages td {
    border-left: 1px solid rgba(255,255,255,.85);
    border-bottom: 1px solid rgba(255,255,255,.85);
    padding: 0 3px; text-align: center;
  }
  .packages th:first-child, .packages td:first-child { border-left: none; text-align: left; }
  .packages th:first-child { text-align: center; }
  .col-name { width: 154px; }
  .col-std { width: 86px; }
  .col-enh { width: 90px; }
  .tick {
    display: inline-block; width: 6px; height: 12px;
    border-right: 1.5px solid var(--white); border-bottom: 1.5px solid var(--white);
    transform: rotate(40deg); margin-top: -3px;
  }
</style>
</head>
<body>

<!-- FRONT SIDE -->
<section class="flyer flyer--front" aria-label="Flyer front side">
  <svg class="layer" width="533" height="752" viewBox="0 0 533 752">
    <defs>
      <linearGradient id="frontPhotoTone" x1="0" y1="0" x2="1" y2="1">
        <stop offset="0" stop-color="#4d9a2a"/>
        <stop offset=".5" stop-color="#c9c0ad"/>
        <stop offset="1" stop-color="#3f8f22"/>
      </linearGradient>
      <linearGradient id="purpleSheen" x1="0" y1="0" x2="1" y2="1">
        <stop offset="0" stop-color="#6a34a6"/>
        <stop offset="1" stop-color="#4e1f8a"/>
      </linearGradient>
    </defs>
    <rect width="533" height="752" fill="url(#purpleSheen)"/>
    <rect width="533" height="330" fill="url(#frontPhotoTone)" role="img" aria-label="Photo of a lush green lawn with a winding paved garden path"/>
    <path d="M0 270 Q200 330 533 292 L533 752 L0 752 Z" fill="#ffffff"/>
    <path d="M0 304 Q220 345 533 326 L533 752 L0 752 Z" fill="url(#purpleSheen)"/>
    <path d="M0 330 Q250 360 533 345 L533 420 Q300 380 0 420 Z" fill="#ffffff" opacity=".05"/>
  </svg>

  <div class="logo-badge" style="left:379px; top:240px;">
    <svg viewBox="0 0 144 144" width="144" height="144">
      <polygon points="72,3 141,72 72,141 3,72" fill="#ffffff" stroke="var(--green)" stroke-width="5"/>
    </svg>
    <div class="logo-name">Pelham<small>Gardening Services</small></div>
  </div>

  <header class="headline">
    <h1 class="headline__main">EXPERT <span>LAWN</span></h1>
    <p class="headline__sub">TREATMENT SERVICES</p>
    <p class="headline__strap">Lawn care by your local gardening expert</p>
  </header>

  <div class="services-tab"><h2>OUR SERVICES</h2></div>
  <ul class="services-list">
    <li>- Lawn Fertilising</li>
    <li>- Scarification</li>
    <li>- Aeration</li>
    <li>- Weed Control</li>
    <li>- Moss Control</li>
    <li>- Hydration Booster</li>
    <li>- Kempix</li>
    <li>- Turfing &amp; Renovation</li>
  </ul>

  <svg class="layer" width="533" height="752" viewBox="0 0 533 752">
    <defs>
      <linearGradient id="hexSpreader" x1="0" y1="0" x2="0" y2="1">
        <stop offset="0" stop-color="#e6e4de"/>
        <stop offset=".6" stop-color="#2f8a3b"/>
        <stop offset="1" stop-color="#5ba832"/>
      </linearGradient>
      <linearGradient id="hexGarden" x1="0" y1="0" x2="0" y2="1">
        <stop offset="0" stop-color="#3c5a32"/>
        <stop offset=".5" stop-color="#4f9a2c"/>
        <stop offset="1" stop-color="#cfc8bb"/>
      </linearGradient>
    </defs>
    <polygon points="278,447 356,447 395,513 356,579 278,579 239,513" fill="url(#hexSpreader)" stroke="#ffffff" stroke-width="4" role="img" aria-label="Photo of a lawn fertiliser spreader being pushed across grass"/>
    <polygon points="399,529 477,529 516,595 477,661 399,661 360,595" fill="url(#hexGarden)" stroke="#ffffff" stroke-width="4" role="img" aria-label="Photo of a neat garden lawn bordered by hedges and a bench"/>
  </svg>

  <p class="services-note">Select a one-off treatment or choose from one of our specially created lawn care packages</p>

  <div class="contact-band">
    <svg class="layer" width="533" height="48" viewBox="0 0 533 48">
      <defs>
        <linearGradient id="grassStrip" x1="0" y1="0" x2="0" y2="1">
          <stop offset="0" stop-color="#7dbd35"/>
          <stop offset="1" stop-color="#3f8a1c"/>
        </linearGradient>
      </defs>
      <rect x="0" y="12" width="270" height="36" fill="url(#grassStrip)" role="img" aria-label="Close-up of grass blades"/>
      <polygon points="265,9 533,9 533,48 258,48" fill="var(--green)"/>
    </svg>
    <p class="contact-phone">01632 960481</p>
    <p class="contact-url">www.pelhamgardening.co.uk/lawncare</p>
  </div>
</section>

<!-- BACK SIDE -->
<section class="flyer flyer--back" aria-label="Flyer back side">
  <svg class="layer" width="533" height="752" viewBox="0 0 533 752">
    <defs>
      <linearGradient id="backPurple" x1="0" y1="0" x2="1" y2="1">
        <stop offset="0" stop-color="#5a2596"/>
        <stop offset="1" stop-color="#6c35a6"/>
      </linearGradient>
      <linearGradient id="backPhotoTone" x1="0" y1="0" x2="1" y2="1">
        <stop offset="0" stop-color="#6d6a4f"/>
        <stop offset=".45" stop-color="#5fb23a"/>
        <stop offset=".8" stop-color="#b7b1a3"/>
        <stop offset="1" stop-color="#4f7f34"/>
      </linearGradient>
    </defs>
    <rect width="533" height="752" fill="url(#backPurple)"/>
    <path d="M0 440 Q180 395 533 430 L533 752 L0 752 Z" fill="#ffffff"/>
    <path d="M0 468 Q200 420 533 446 L533 752 L0 752 Z" fill="url(#backPhotoTone)" role="img" aria-label="Photo of a striped lawn with a curving stone path, flower borders and a garden seat"/>
  </svg>

  <div class="intro">
    <p>As expert gardeners, we are passionate about horticulture and working to bring out the very best in your garden. When we work in your garden, we look at it and treat it with the same care and attention as if it were our own, before handing it back for you to enjoy. Our passion doesn't end at just trees and shrubs though. Your grass is as much of a living, breathing plant as your shrubs and we therefore utilise our expert horticultural knowledge to ensure your lawn thrives and reaches its fullest potential.</p>
    <p>Lawn care isn't just about applying a fertiliser. It's about really understanding your lawn and being able to use extensive knowledge and experience to diagnose and treat issues. It therefore stands to reason that you should employ an expert to bring out the best in your lawn which is why we at Pelham Gardening Services have created a superior lawn care service that will keep your lawn looking lush, green and healthy all year round.</p>
  </div>

  <div class="packages">
    <h2 class="packages__title">Lawn Treatment Packages</h2>
    <table>
      <thead>
        <tr><th class="col-name">Services name</th><th class="col-std">Standard</th><th class="col-enh">Enchanted</th><th>Premium</th></tr>
      </thead>
      <tbody>
        <tr><td>Spring Treatment</td><td><i class="tick"></i></td><td><i class="tick"></i></td><td><i class="tick"></i></td></tr>
        <tr><td>Early Summer Treatment</td><td><i class="tick"></i></td><td><i class="tick"></i></td><td><i class="tick"></i></td></tr>
        <tr><td>Late Summer Treatment</td><td><i class="tick"></i></td><td><i class="tick"></i></td><td><i class="tick"></i></td></tr>
        <tr><td>Autumn/Winter Treatment</td><td><i class="tick"></i></td><td><i class="tick"></i></td><td><i class="tick"></i></td></tr>
        <tr><td>Scarification</td><td></td><td><i class="tick"></i></td><td><i class="tick"></i></td></tr>
        <tr><td>Aeration</td><td></td><td><i class="tick"></i></td><td><i class="tick"></i></td></tr>
        <tr><td>Kempix Treatment</td><td></td><td></td><td><i class="tick"></i></td></tr>
        <tr><td>Hydration Boost Treatment</td><td></td><td></td><td><i class="tick"></i></td></tr>
      </tbody>
    </table>
  </div>

  <div class="logo-badge" style="left:170px; top:610px;">
    <svg viewBox="0 0 144 144" width="144" height="144">
      <polygon points="72,3 141,72 72,141 3,72" fill="#ffffff" stroke="var(--green)" stroke-width="5"/>
    </svg>
    <div class="logo-name">Pelham<small>Gardening Services</small></div>
  </div>

  <div class="contact-band">
    <svg class="layer" width="533" height="48" viewBox="0 0 533 48">
      <rect x="0" y="12" width="230" height="36" fill="url(#grassStrip)" role="img" aria-label="Close-up of grass blades"/>
      <polygon points="300,9 533,9 533,48 300,48" fill="var(--green)"/>
    </svg>
    <p class="contact-phone">01632 960481</p>
    <p class="contact-url">www.pelhamgardening.co.uk/lawncare</p>
  </div>
</section>

</body>
</html>
```